Exclusive Social Networking Platform for future CEOs (no coding required)

We need a creative remake design (from rough mock-ups) for our social networking platform. We are a US-based start-up company called Circle Brightpath. Our platform allows high-caliber students and young professionals that are part of established networks to reconnect online. It also has an element of Roomtrader.com (host exchange system). In terms of the layout, it can therefore be considered a combination of:
- Jobvista (CV style profiles)
- Chatterbox (messaging, pictures, posts, etc.)
- Roomtrader

UPDATE: We have been asking a few people to try to implement a map of the world (maybe just the outlines) as a backdrop to the platform, but in such a way that it is only faintly noticeable and doesn't become distracting to the platform.

If we really like your designs we may approach you for future designs for a collection of other businesses on a freelance basis (we work out of an incubator).

CONDITIONS: We are only asking for 2 pages as examples (attached PDFs). There may be an opportunity for you to design the rest of the platform as well.
Updates

Thank you very much for your designs so far! There are some very good ones among them. 

Reason: We are still waiting on several designers to provide their edited versions, and we have not yet found the designs we are looking for.

Target Market(s)

Our users are:
1. high-potential global students and young professionals
2. that have been selected to participate in high-end conferences & networks
3. and are typically entrepreneurs, techies, or young corporates
4. they love to travel
5. they are very ambitious about their careers
6. they spend a lot of time meeting people and networking

Industry/Entity Type

It Company

Requirements
Must have
• Base colours (can contain any combination of the following—you can also exclude blue if you like):
- Dark grey (almost black)
- lighter greys
- white
- blue

In terms of the design, please base it on the functional layouts we have provided (attached files). Feel free to redesign as you wish (both in colour and structure), as long as it keeps the functionality outlined by the rough sketches.
- please redesign the icons at the top (News Feed, Events, HomeLoop, Expeditions) to a very simple and attractive format

NOTE: Please provide one design for each of the 2 PDF files ('WaveRoam' and 'Profile') to show us how you creatively visualise the platform ('WaveRoam' is the most up-to-date version considering the icons on the top and the general layout). Please also consider the attached logo to get a feeling of our brand.
Nice to have
• We would be happy to see a creative infusion of the colourful colours of our logo (see attached file). With this, it would be important that it would be kept to a minimum (as otherwise it will be distracting), so a good place to include it may be in the icons that direct people around the site, or in other parts that are more creative—up to you!

```html
<!DOCTYPE html>
<html lang="en">
<head>
<meta charset="utf-8">
<title>Circle Brightpath – Profile</title>
<link rel="stylesheet" href="https://fonts.googleapis.com/css2?family=Open+Sans:ital,wght@0,400;0,600;0,700;1,700&display=swap">
<style>
:root{
  --ink:#1b1b1b;
  --white:#ffffff;
  --topbar-a:#ffffff;
  --topbar-b:#dcdcdc;
  --band-a:#5a5a5a;
  --band-b:#2b2b2b;
  --blue:#1a73c8;
  --blue-bright:#0b7fd6;
  --panel:#f2f2f2;
  --panel-edge:#c9c9c9;
  --track:#c4c4c4;
  --online:#19c24a;
  --hero-a:#3b1f6e;
  --hero-b:#b04a8c;
  --hero-c:#e08a4a;
  --hero-d:#5a3a28;
  --hero-e:#1a1a1a;
}
*{box-sizing:border-box;margin:0;padding:0}
html,body{width:1200px;height:938px;overflow:hidden}
body{position:relative;font-family:"Open Sans",Arial,sans-serif;color:var(--ink);background:var(--hero-e)}
.abs{position:absolute}

/* top bar */
.topbar{left:0;top:0;width:1200px;height:65px;background:linear-gradient(var(--topbar-a),var(--topbar-b))}
.brand{left:42px;top:12px;display:flex;align-items:center;gap:12px}
.brand-dot{width:34px;height:34px;border-radius:50%;background:var(--blue)}
.brand-name{font-size:28px;font-weight:600;color:var(--ink);letter-spacing:.5px}
.search{left:474px;top:14px;width:300px;height:32px;border-radius:16px;background:#e4e4e4;border:1px solid #bdbdbd;box-shadow:inset 0 2px 3px rgba(0,0,0,.2);font-size:14px;line-height:30px;padding-left:44px;color:#222;white-space:nowrap}
.top-icon{top:13px;width:40px;height:40px}

/* dark band + nav */
.band{left:0;top:65px;width:1200px;height:127px;background:linear-gradient(var(--band-a),var(--band-b))}
.nav{left:230px;top:74px;width:740px;height:101px;background:var(--white);border-radius:16px}
.nav-item{top:0;width:150px;height:101px;text-align:center}
.nav-item svg{position:absolute;left:45px;top:10px;width:60px;height:56px}
.nav-item span{position:absolute;left:0;right:0;top:73px;font-size:19px;font-weight:700;white-space:nowrap}

/* hero */
.hero-bg{left:0;top:192px;width:1200px;height:746px;background:
  radial-gradient(ellipse at 55% 40%,rgba(224,138,74,.75),transparent 55%),
  linear-gradient(180deg,var(--hero-a) 0%,var(--hero-b) 22%,var(--hero-d) 50%,var(--hero-e) 80%)}
.hero-card{left:96px;top:206px;width:1062px;height:260px;background:rgba(40,30,40,.35)}
.portrait{left:104px;top:220px;width:168px;height:228px;background:linear-gradient(160deg,#a49a88,#d8d0c4 60%,#7b7266)}
.name{left:326px;top:222px;font-size:53px;line-height:72px;font-weight:700;font-style:italic;color:var(--white);white-space:nowrap}
.role{left:327px;top:320px;font-size:21px;line-height:28px;font-weight:700;color:var(--white);white-space:nowrap}
.facts{left:327px;top:346px;font-size:15.5px;font-weight:700;color:var(--white);line-height:20px;white-space:nowrap}

/* side panels */
.panel{background:var(--panel);border:1px solid var(--panel-edge)}
.networks{left:20px;top:508px;width:208px;height:110px}
.panel-title{font-size:16px;line-height:22px;font-weight:700;color:var(--blue);white-space:nowrap}
.networks .panel-title{position:absolute;left:10px;top:4px}
.networks ul{position:absolute;left:16px;top:26px;list-style:none;font-size:12.5px;line-height:17px;white-space:nowrap}
.scroll{position:absolute;width:14px;background:var(--track)}
.scroll i{position:absolute;left:2px;width:10px;background:var(--blue);border-radius:1px}

.chat-panel{left:20px;top:637px;width:208px;height:301px;overflow:hidden}
.chat-search{position:absolute;left:12px;top:5px;width:156px;height:18px;border-radius:9px;background:#dcdcdc;font-size:13px;font-weight:600;color:var(--blue);text-align:center;line-height:18px}
.people{position:absolute;left:8px;top:37px;list-style:none;font-size:14.5px;line-height:18.9px}
.people li{padding-left:16px;position:relative}
.people li.on::before{content:"";position:absolute;left:1px;top:6px;width:7px;height:7px;border-radius:50%;background:var(--online)}

/* main card */
.tabs{left:264px;top:505px;width:688px;height:43px;background:linear-gradient(#fafafa,#dedede);border:1px solid var(--panel-edge);display:flex}
.tab{height:100%;font-size:17px;font-weight:600;text-align:center;line-height:41px;border-right:1px solid #b9b9b9;white-space:nowrap}
.tab:last-child{border-right:0}
.content{left:264px;top:548px;width:688px;height:390px;background:var(--white)}
.content h2{position:absolute;left:26px;font-size:18px;line-height:22px;font-weight:700;white-space:nowrap}
.content p,.row{position:absolute;left:26px;font-size:15.5px;line-height:21px;color:#222}
.row{white-space:nowrap}
.row .yr{display:inline-block;width:108px}

/* events */
.events{left:991px;top:505px;width:192px;height:433px}
.events .panel-title{position:absolute;left:14px;top:8px;font-style:italic}
.event{position:absolute;left:12px;width:156px}
.event b{display:block;font-size:16.5px;line-height:22px;font-weight:700;color:var(--blue-bright);word-spacing:8px;white-space:nowrap}
.event span{display:block;font-size:12.5px;line-height:17.5px;color:#333}

.chat-tab{top:914px;height:24px;background:var(--blue-bright);color:var(--white);font-size:16px;font-weight:700;text-align:center;line-height:24px;white-space:nowrap}
.chat-tab .dot{display:inline-block;width:8px;height:8px;border-radius:50%;background:var(--online);margin-right:8px;vertical-align:2px}
</style>
</head>
<body>

<header class="abs topbar"></header>
<div class="abs brand"><span class="brand-dot"></span><span class="brand-name">Circle Brightpath</span></div>
<div class="abs search">Search for people, places or network</div>

<svg class="abs top-icon" style="left:890px" viewBox="0 0 40 40" aria-label="Contacts">
  <rect x="2" y="2" width="36" height="36" rx="6" fill="#e8e8e8" stroke="#555"/>
  <circle cx="15" cy="14" r="5" fill="#1a73c8"/><path d="M6 32c0-7 4-11 9-11s9 4 9 11z" fill="#1a73c8"/>
  <circle cx="26" cy="13" r="5" fill="#1a73c8"/><path d="M17 30c0-7 4-11 9-11s9 4 9 11z" fill="#1a73c8"/>
</svg>
<svg class="abs top-icon" style="left:978px;width:52px" viewBox="0 0 52 40" aria-label="Messages">
  <path d="M4 10c0-5 6-8 16-8s16 3 16 8-6 8-16 8l-7 5 1-5C8 18 4 15 4 10z" fill="#1a73c8" stroke="#333"/>
  <path d="M16 22c0-5 7-8 16-8s17 3 17 8-7 8-16 8l-1 6-6-6c-6-1-10-4-10-8z" fill="#3b9be0" stroke="#333"/>
</svg>
<svg class="abs top-icon" style="left:1066px" viewBox="0 0 40 40" aria-label="Profile">
  <circle cx="20" cy="9" r="6" fill="#1a73c8"/><rect x="12" y="17" width="16" height="21" rx="5" fill="#1a73c8"/>
</svg>
<svg class="abs top-icon" style="left:1130px" viewBox="0 0 40 40" aria-label="Settings">
  <g fill="#e8e8e8" stroke="#444" stroke-width="2">
    <path d="M17 2h6l1 5 4 2 4-3 4 4-3 4 2 4 5 1v6l-5 1-2 4 3 4-4 4-4-3-4 2-1 5h-6l-1-5-4-2-4 3-4-4 3-4-2-4-5-1v-6l5-1 2-4-3-4 4-4 4 3 4-2z"/>
    <circle cx="20" cy="20" r="6"/>
  </g>
</svg>

<div class="abs band"></div>
<nav class="abs nav">
  <div class="abs nav-item" style="left:0">
    <svg viewBox="0 0 60 56"><rect x="4" y="10" width="52" height="36" rx="3" fill="#f4f4f4" stroke="#555" stroke-width="2"/><rect x="10" y="16" width="40" height="7" fill="#888"/><g stroke="#999" stroke-width="2"><path d="M10 29h18M10 34h18M10 39h18M32 29h18M32 34h18M32 39h18"/></g></svg>
    <span>News Feed</span>
  </div>
  <div class="abs nav-item" style="left:161px">
    <svg viewBox="0 0 60 56"><rect x="8" y="4" width="44" height="48" rx="3" fill="#29a3e8"/><rect x="8" y="4" width="44" height="10" fill="#1a73c8"/><g fill="#fff"><rect x="12" y="18" width="7" height="6"/><rect x="22" y="18" width="7" height="6"/><rect x="32" y="18" width="7" height="6"/><rect x="42" y="18" width="7" height="6"/><rect x="12" y="28" width="7" height="6"/><rect x="22" y="28" width="7" height="6"/><rect x="32" y="28" width="7" height="6"/><rect x="42" y="28" width="7" height="6"/><rect x="12" y="38" width="7" height="6"/><rect x="22" y="38" width="7" height="6"/><rect x="32" y="38" width="7" height="6"/><rect x="42" y="38" width="7" height="6"/></g></svg>
    <span>Events</span>
  </div>
  <div class="abs nav-item" style="left:299px">
    <svg viewBox="0 0 60 56"><g fill="#1a73c8"><circle cx="30" cy="14" r="7"/><path d="M19 40c0-10 5-16 11-16s11 6 11 16z"/></g><g fill="#7a7a7a"><circle cx="13" cy="22" r="5"/><path d="M5 44c0-8 4-13 8-13s8 5 8 13z"/><circle cx="47" cy="22" r="5"/><path d="M39 44c0-8 4-13 8-13s8 5 8 13z"/></g></svg>
    <span>Networks</span>
  </div>
  <div class="abs nav-item" style="left:458px">
    <svg viewBox="0 0 60 56"><circle cx="30" cy="28" r="24" fill="#2e8fe0"/><g fill="none" stroke="#bfe3ff" stroke-width="1.5"><ellipse cx="30" cy="28" rx="10" ry="24"/><path d="M6 28h48M10 16h40M10 40h40"/></g></svg>
    <span>HomeLoop</span>
  </div>
  <div class="abs nav-item" style="left:595px">
    <svg viewBox="0 0 60 56"><circle cx="30" cy="28" r="24" fill="#2a4a66" stroke="#777" stroke-width="3"/><circle cx="30" cy="28" r="19" fill="#3a78a8"/><path d="M40 16 33 31 20 40 27 25z" fill="#fff"/><path d="M40 16 33 31 27 25z" fill="#e04040"/></svg>
    <span>Expeditions</span>
  </div>
</nav>

<div class="abs hero-bg" role="img" aria-label="Backdrop photo of a grand lit hotel facade at dusk with fountains"></div>
<div class="abs hero-card"></div>
<div class="abs portrait" role="img" aria-label="Profile photo of the member"></div>
<h1 class="abs name">Marco Velasquez Hart</h1>
<div class="abs role">Co-Founder of Circle Brightpath and Summit Lodge</div>
<div class="abs facts">
  Membership :<br>
  Mission in Life : Turning Acquiantence into friendship and saving the rain forests<br>
  Based in :&nbsp; Ashbridge , UK<br>
  Current Location : Ashbridge , UK
</div>

<aside class="abs panel networks">
  <div class="panel-title">My NetWorks</div>
  <ul><li>Global Venture Forum</li><li>Meridia</li><li>NSEC</li><li>Latin Founders Circle....</li></ul>
  <div class="scroll" style="left:180px;top:14px;height:80px"><i style="top:4px;height:32px"></i></div>
</aside>

<aside class="abs panel chat-panel">
  <div class="chat-search">Search Chat</div>
  <ul class="people">
    <li class="on">Daniel</li><li class="on">Strom Elite</li><li class="on">Tom</li><li class="on">Mike ketoe</li><li class="on">Chui Chan</li><li class="on">Larrie cloid</li><li class="on">Ethan</li>
    <li>Robert</li><li>Julian</li><li>Samest</li><li>Trutheee</li><li>Rahel</li><li>Abdul</li><li>Bharat</li>
  </ul>
  <div class="scroll" style="left:180px;top:32px;height:269px"><i style="top:3px;height:38px"></i></div>
</aside>

<div class="abs tabs">
  <div class="tab" style="width:112px">CV</div>
  <div class="tab" style="width:163px">About me</div>
  <div class="tab" style="width:237px">Host and Travel</div>
  <div class="tab" style="flex:1">Photos</div>
</div>

<main class="abs content">
  <h2 style="top:24px">Professional Summary</h2>
  <p style="top:48px;width:620px">I am a recent Graduate from Harrowgate University ,UK and decided that emoyement is boring.</p>
  <h2 style="top:136px">Higher Education</h2>
  <div class="row" style="top:165px"><span class="yr">2009-2012</span>Harrowgate University</div>
  <div class="row" style="top:192px"><span class="yr">2008-2009</span>Harrowgate University</div>
  <h2 style="top:246px">Work Experience</h2>
  <div class="row" style="top:274px"><span class="yr">April-2013</span>Circle Brightpath</div>
  <div class="row" style="top:301px;left:125px">Cofounder and CEO of Circle Brightpath</div>
</main>

<aside class="abs panel events">
  <div class="panel-title">Events &amp; Dead lines</div>
  <div class="event" style="top:46px"><b>Today 13th Sept</b><span>Global Venture Forum Ambassidor application for the 16th GVF closing</span></div>
  <div class="event" style="top:133px"><b>Today 13th Sept</b><span>Global Venture Forum Ambassidor application for the 16th GVF closing</span></div>
  <div class="event" style="top:217px"><b>Today 13th Sept</b><span>Global Venture Forum Ambassidor application for the 16th GVF closing</span></div>
  <div class="event" style="top:310px"><b>Today 13th Sept</b><span>Global Venture Forum Ambassidor application for the 16th GVF closing</span></div>
  <div class="scroll" style="left:170px;top:48px;height:385px"><i style="top:4px;height:40px"></i></div>
</aside>

<div class="abs chat-tab" style="left:668px;width:143px"><span class="dot"></span>Ethan</div>
<div class="abs chat-tab" style="left:830px;width:143px"><span class="dot"></span>Daniel</div>
<div class="abs chat-tab" style="left:996px;width:170px">Chat&nbsp; (7)</div>

</body>
</html>
```